Need business cards for our e-assessment business

We need professional looking business cards for our e-assessment business based in Europe. Our company is called Velmora.

You can just use sample name and addresses.

The colours we use are:

#70abe4 (blue)
#FF6600 (orange)

The back side should say: E-assessment made easy

This is the print-shop we are using. Please look at the link for info about formats: http://nl.pribbly-print.com/help/faq/using-my-own-artwork.html

Target Market(s)

Target market is education and large corporations

Industry/Entity Type

Business

```html
<!DOCTYPE html>
<html lang="en">
<head>
<meta charset="utf-8">
<title>Velmora – Business Cards</title>
<link rel="stylesheet" href="https://fonts.googleapis.com/css2?family=Open+Sans:wght@300;400;600&display=swap">
<style>
  :root {
    --brand-blue: #70abe4;
    --brand-orange: #ff6600;
    --card-white: #fbfbfb;
    --ink: #3d3f45;
    --ink-soft: #4b4f58;
    --backdrop: #4a4b4e;
    --font-main: "Open Sans", Arial, sans-serif;
  }
  html, body {
    margin: 0;
    padding: 0;
    width: 1200px;
    height: 873px;
    overflow: hidden;
    background: var(--backdrop);
    font-family: var(--font-main);
  }
  .sheet {
    position: relative;
    width: 1200px;
    height: 873px;
  }
  .card {
    position: absolute;
    top: 274px;
    width: 500px;
    height: 324px;
    background: var(--card-white);
    overflow: hidden;
    box-shadow: 0 6px 18px rgba(0, 0, 0, 0.35);
  }
  .card--front { left: 70px; }
  .card--back  { left: 630px; }

  /* Front */
  .front-arc {
    position: absolute;
    left: 0;
    top: 0;
  }
  .brand {
    position: absolute;
    left: 30px;
    top: 30px;
    display: flex;
    align-items: center;
    gap: 12px;
  }
  .brand__dot {
    width: 46px;
    height: 46px;
    border-radius: 50%;
    background: var(--brand-orange);
  }
  .brand__name {
    font-weight: 300;
    font-size: 42px;
    line-height: 1;
    color: var(--ink);
    letter-spacing: -0.5px;
  }
  .contact {
    position: absolute;
    left: 300px;
    top: 58px;
  }
  .contact__name {
    margin: 0;
    font-weight: 600;
    font-size: 13px;
    color: #ffffff;
    padding-left: 22px;
  }
  .contact__role {
    margin: 2px 0 18px;
    font-size: 11px;
    color: var(--ink-soft);
    padding-left: 22px;
  }
  .contact__list {
    list-style: none;
    margin: 0;
    padding: 0;
  }
  .contact__item {
    display: flex;
    align-items: center;
    height: 20px;
    font-size: 11px;
    color: var(--ink-soft);
  }
  .contact__item svg {
    width: 12px;
    height: 12px;
    margin-right: 10px;
    flex: none;
  }
  .contact__item--web {
    margin-top: 10px;
    color: var(--brand-orange);
  }

  /* Back */
  .back-mark {
    position: absolute;
    left: 50%;
    top: 62px;
    width: 132px;
    height: 132px;
    margin-left: -66px;
    border-radius: 50%;
    background: var(--brand-orange);
  }
  .tagline {
    position: absolute;
    left: 0;
    right: 0;
    top: 222px;
    margin: 0;
    text-align: center;
    font-weight: 400;
    font-size: 26px;
    letter-spacing: 0.2px;
  }
  .tagline__lead { color: var(--brand-blue); }
  .tagline__end  { color: var(--brand-orange); }
</style>
</head>
<body>
<main class="sheet">

  <section class="card card--front" aria-label="Business card front">
    <svg class="front-arc" width="500" height="324" viewBox="0 0 500 324" aria-hidden="true">
      <circle cx="600" cy="-60" r="470" fill="var(--brand-blue)"/>
    </svg>

    <div class="brand">
      <span class="brand__dot" aria-hidden="true"></span>
      <span class="brand__name">Velmora</span>
    </div>

    <div class="contact">
      <p class="contact__name">Daan Verhoef</p>
      <p class="contact__role">Co-founder &amp; CEO</p>
      <ul class="contact__list">
        <li class="contact__item">
          <svg viewBox="0 0 12 12" aria-hidden="true"><path d="M2.5 1h2l1 2.5-1.3 1a6 6 0 0 0 2.8 2.8l1-1.3 2.5 1v2a1 1 0 0 1-1 1A9 9 0 0 1 1.5 2a1 1 0 0 1 1-1z" fill="var(--brand-orange)"/></svg>
          (+31) 412 7390
        </li>
        <li class="contact__item">
          <svg viewBox="0 0 12 12" aria-hidden="true"><path d="M2.5 1h2l1 2.5-1.3 1a6 6 0 0 0 2.8 2.8l1-1.3 2.5 1v2a1 1 0 0 1-1 1A9 9 0 0 1 1.5 2a1 1 0 0 1 1-1z" fill="var(--brand-orange)"/></svg>
          (+31) 528 4461
        </li>
        <li class="contact__item">
          <svg viewBox="0 0 12 12" aria-hidden="true"><rect x="3" y="0.5" width="6" height="11" rx="1" fill="var(--brand-orange)"/><rect x="4" y="2" width="4" height="7" fill="var(--brand-blue)"/></svg>
          0642 918 305
        </li>
        <li class="contact__item">
          <svg viewBox="0 0 12 12" aria-hidden="true"><rect x="3" y="1" width="6" height="3" fill="var(--brand-orange)"/><rect x="1" y="4" width="10" height="5" rx="1" fill="var(--brand-orange)"/><rect x="3" y="8" width="6" height="3" fill="var(--brand-orange)"/></svg>
          +31 873 2254
        </li>
        <li class="contact__item">
          <svg viewBox="0 0 12 12" aria-hidden="true"><rect x="1" y="2.5" width="10" height="7" fill="none" stroke="var(--brand-orange)" stroke-width="1.3"/><path d="M1 2.5l5 4 5-4" fill="none" stroke="var(--brand-orange)" stroke-width="1.3"/></svg>
          hello@velmora-mail.eu
        </li>
        <li class="contact__item contact__item--web">
          <svg viewBox="0 0 12 12" aria-hidden="true"><circle cx="6" cy="6" r="5" fill="none" stroke="var(--brand-orange)" stroke-width="1.2"/><ellipse cx="6" cy="6" rx="2.2" ry="5" fill="none" stroke="var(--brand-orange)" stroke-width="1"/><path d="M1 6h10M2 3.5h8M2 8.5h8" stroke="var(--brand-orange)" stroke-width="0.9"/></svg>
          www.velmora.eu
        </li>
      </ul>
    </div>
  </section>

  <section class="card card--back" aria-label="Business card back">
    <div class="back-mark" aria-hidden="true"></div>
    <p class="tagline">
      <span class="tagline__lead">E-assessment</span>
      <span class="tagline__end">made easy</span>
    </p>
  </section>

</main>
</body>
</html>
```